Landing page for 'Page under construction' page

We need a simple landing page that we can use while our page is under construction.

The page should be made ready so that all we need to do is drop it on our web server and then it will function as our webpage. The domain is www.tlv-demo.no

Please see attached file for instructions on what elements to include in the landing page. The Brand Book provides fonts and color palette.

Coding

Coded - Design and coding required

Number of Pages Required

1 page

Colors

Designer to choose colors to be used in the design.

```html
<!DOCTYPE html>
<html lang="en">
<head>
<meta charset="utf-8">
<title>TLV Consulting – Page under construction</title>
<link href="https://fonts.googleapis.com/css2?family=Montserrat:wght@400;500;600;700;800;900&display=swap" rel="stylesheet">
<style>
:root{
  --navy:#07336a;
  --navy-text:#0b3270;
  --accent-blue:#2d86c8;
  --coral:#ea5455;
  --orange:#f29a45;
  --white:#ffffff;
  --ink:#111111;
  --pale:#eaf2fb;
  --line:#6b93c9;
  --mint:#76c9b3;
}
*{margin:0;padding:0;box-sizing:border-box}
html,body{width:750px;height:1200px;overflow:hidden;background:var(--white)}
body{font-family:"Montserrat",sans-serif;color:var(--ink);position:relative}

.hero{position:absolute;left:0;top:0;width:750px;height:420px;background:var(--navy);color:var(--white)}
.brand{position:absolute;left:26px;top:24px;display:flex;align-items:center;gap:6px;font-weight:800;font-size:18px;letter-spacing:.2px}
.brand-dot{width:8px;height:8px;border-radius:50%;background:var(--white)}
.main-nav{position:absolute;left:280px;top:28px;display:flex;gap:18px;font-size:9.5px;font-weight:500}
.cta{position:absolute;left:629px;top:22px;width:84px;height:22px;border-radius:11px;background:linear-gradient(90deg,var(--coral),var(--orange));font-size:7px;font-weight:700;display:flex;align-items:center;justify-content:center;letter-spacing:.4px}
.hero-title{position:absolute;left:30px;top:148px;font-weight:900;font-size:28px;line-height:1.15;letter-spacing:.3px}
.hero-rule{position:absolute;left:33px;top:223px;width:88px;height:3px;background:var(--coral)}
.hero-copy{position:absolute;left:30px;top:248px;width:240px;font-size:6.4px;font-weight:500;line-height:1.32}
.hero-copy p+p{margin-top:7px}
.hero-art{position:absolute;left:360px;top:70px;width:380px;height:350px;border-radius:6px;background:linear-gradient(160deg,#0d3f7a 0%,#6fbfa9 55%,#f0b646 100%);opacity:.9}

.vision{position:absolute;left:0;top:420px;width:750px;height:470px}
.section-title{font-weight:700;color:var(--navy-text);text-align:center}
.vision .section-title{position:absolute;left:0;width:750px;top:34px;font-size:21px}
.title-rule{position:absolute;height:2px;background:var(--coral)}
.item{position:absolute;left:55px;width:660px}
.item-icon{position:absolute;left:0;top:0}
.item h3{position:absolute;left:100px;top:0;font-size:11px;font-weight:600;color:var(--accent-blue);white-space:nowrap}
.item p{position:absolute;left:102px;top:18px;font-size:8.4px;line-height:1.3}
.diagram{position:absolute;left:168px;top:292px;width:414px;height:170px}

.connect{position:absolute;left:0;top:890px;width:750px;height:290px;background:var(--pale)}
.divider{position:absolute;left:374px;top:0;width:1px;height:290px;background:var(--line)}
.or{position:absolute;left:358px;top:142px;width:34px;text-align:center;background:var(--pale);font-weight:700;font-size:10px;color:var(--navy-text);padding:4px 0}
.subscribe .section-title{position:absolute;left:60px;width:270px;top:70px;font-size:19px;line-height:1.25}
.field{position:absolute;background:var(--white);border:1px solid #e3ebf4;font-size:5.5px;color:#555;padding:8px 9px}
.btn{position:absolute;border-radius:14px;background:linear-gradient(90deg,var(--coral),var(--orange));color:var(--white);font-weight:700;font-size:9px;letter-spacing:.5px;display:flex;align-items:center;justify-content:center}
.contact .section-title{position:absolute;left:400px;width:320px;top:20px;font-size:19px}
.page-foot{position:absolute;left:0;top:1180px;width:750px;height:20px;background:var(--white)}
</style>
</head>
<body>

<header class="hero">
  <div class="brand"><span class="brand-dot"></span>tellvik</div>
  <nav class="main-nav">
    <span>EPM</span><span>Low-Code</span><span>Customers</span><span>Resources</span><span>About</span><span>EN ▾</span>
  </nav>
  <div class="cta">TALK TO US</div>
  <h1 class="hero-title">PAGE IS UNDER<br>CONSTRUCTION</h1>
  <div class="hero-rule"></div>
  <div class="hero-copy">
    <p>Digital solutions and data-driven business development that create value.</p>
    <p>TLV Consulting is a consulting company with cutting-edge expertise in digitalisation and data-driven business development. We have extensive experience in data warehouse development, data analysis and reporting, EPM and planning solutions, budget and forecasting solutions for financial and financial data. In short, we help our customers exploit the potential in the available data.</p>
  </div>
  <div class="hero-art" role="img" aria-label="Illustration of construction workers painting and repairing a web page, with ladders, traffic cones and an under construction barrier"></div>
</header>

<section class="vision">
  <h2 class="section-title">TLV vision and TLV focus</h2>
  <div class="title-rule" style="left:352px;top:66px;width:46px"></div>

  <div class="item" style="top:104px">
    <svg class="item-icon" width="32" height="16" viewBox="0 0 32 16">
      <path d="M1 8 Q16 -4 31 8 Q16 20 1 8Z" fill="#2d6fb5"/>
      <circle cx="16" cy="8" r="6" fill="#fff"/>
      <circle cx="16" cy="8" r="4.5" fill="#2d86c8"/>
      <circle cx="16" cy="8" r="2.2" fill="#fff"/>
      <circle cx="16" cy="8" r="1.2" fill="#2d86c8"/>
    </svg>
    <h3 style="left:113px">TLV Vision</h3>
    <p style="left:116px">TLV will be the country's leading supplier and competence house on<br>Tellvik software and digital solutions for business management.</p>
  </div>

  <div class="item" style="top:158px">
    <svg class="item-icon" width="22" height="22" viewBox="0 0 22 22" style="left:5px">
      <circle cx="11" cy="11" r="8" fill="none" stroke="#2d86c8" stroke-width="1.6"/>
      <circle cx="11" cy="11" r="4" fill="none" stroke="#2d86c8" stroke-width="1.4"/>
      <path d="M11 0V6M11 16V22M0 11H6M16 11H22" stroke="#2d86c8" stroke-width="1.4"/>
    </svg>
    <h3 style="left:113px">TLV Focus</h3>
    <p style="left:113px;width:455px">I TLV Focus er vi brennende opptatt av å utvikle gode løsninger som støtter opp om kundens digitale strategi. Vi har spesialisert oss på å levere konsulenttjenester og løsninger innenfor datavarehus, datavisualisering, integrasjoner og maskinlæring for store kunder over hele landet. Felles for disse er bruk av nyeste teknologi, hovedsakelig på Nimbus plattformen, der vi som leverandør ivaretar flere roller som rådgivere, arkitekter og utviklere. Vi utvikler dataplattformer i Nimbus Cloud og har bred kompetanse på utvikling og implementering av Insight Studio. Vi utvikler integrasjoner som sørger for flyt og utveksling av data mellom systemer, samarbeidspartnere og sluttkunder. Vi utvikler maskinlæringsmodeller som effektiviserer og forenkler kundens hverdag.</p>
  </div>

  <svg class="diagram" viewBox="0 0 414 170" font-family="Montserrat, sans-serif">
    <defs>
      <linearGradient id="panelBg" x1="0" x2="1"><stop offset="0" stop-color="#6d8db6"/><stop offset=".6" stop-color="#4b5d79"/><stop offset="1" stop-color="#2a2b30"/></linearGradient>
      <linearGradient id="boxBg" x1="0" x2="1"><stop offset="0" stop-color="#f29a45"/><stop offset="1" stop-color="#ea5455"/></linearGradient>
    </defs>
    <rect width="414" height="170" fill="url(#panelBg)"/>
    <text x="40" y="30" font-size="5" fill="#fff">Tellvik Focus</text>
    <text x="230" y="30" font-size="5" fill="#fff">TLV Consulting</text>
    <rect x="37" y="35" width="154" height="58" fill="url(#boxBg)"/>
    <rect x="227" y="35" width="154" height="58" fill="url(#boxBg)"/>
    <g font-size="4.6" fill="#fff" font-weight="500">
      <text x="41" y="54">VI SKAL VÆRE EN LEDENDE LEVERANDØR AV BI</text>
      <text x="41" y="62">KONSULENTTJENESTER OG LØSNINGER FOR</text>
      <text x="41" y="70">FORRETNINGSSTØTTE OG VIRKSOMHETSSTYRING,</text>
      <text x="41" y="78">HOVEDSAKELIG PÅ NIMBUS PLATTFORMEN</text>
      <text x="231" y="53">VI SKAL VÆRE LANDETS LEDENDE LEVERANDØR OG</text>
      <text x="231" y="61">KOMPETANSEHUS PÅ TELLVIK PROGRAMVARE</text>
      <text x="231" y="69">OG DIGITALE LØSNINGER FOR</text>
      <text x="231" y="77">VIRKSOMHETSSTYRING</text>
    </g>
    <g stroke="#cfd7e3" stroke-width=".6" fill="none">
      <path d="M114 93V116M304 93V116M40 116H376"/>
      <path d="M40 116V130M171 116V130M239 116V130M307 116V130M376 116V130"/>
    </g>
    <path d="M34 148a4 4 0 0 1 3-6 5 5 0 0 1 9 1 3 3 0 0 1 1 5Z" fill="#fff"/>
    <rect x="165" y="136" width="12" height="10" fill="none" stroke="#fff" stroke-width="1"/>
    <path d="M168 144V141M171 144V138M174 144V140" stroke="#fff" stroke-width="1.4"/>
    <path d="M239 136V141M233 141H245M233 141V145M245 141V145M239 141V145" stroke="#fff" stroke-width="1"/>
    <rect x="231" y="145" width="4" height="3" fill="#fff"/><rect x="237" y="145" width="4" height="3" fill="#fff"/><rect x="243" y="145" width="4" height="3" fill="#fff"/>
    <path d="M303 137h3v10h-4ZM308 137h3l1 10h-4Z" fill="#fff"/>
    <rect x="369" y="136" width="14" height="10" fill="none" stroke="#fff" stroke-width="1"/>
    <text x="371.5" y="144" font-size="5" fill="#fff">&lt;/&gt;</text>
    <g font-size="5" fill="#fff" font-weight="700">
      <text x="56" y="141">• DATAVAREHUS</text>
      <text x="56" y="148">• DATAVISUALISERING</text>
      <text x="56" y="155">• INTEGRASJONER</text>
      <text x="56" y="162">• MASKINLÆRING</text>
      <text x="132" y="162">BUSINESS INTELLIGENCE</text>
      <text x="216" y="162">CONSOLIDATION</text>
      <text x="290" y="162">PLANNING</text>
      <text x="345" y="162">CUSTOME SOLUTIONS</text>
    </g>
  </svg>
</section>

<section class="connect">
  <div class="divider"></div>
  <div class="or">Or</div>

  <div class="subscribe">
    <h2 class="section-title">Subscribe to<br>OurNewsletter</h2>
    <div class="title-rule" style="left:174px;top:132px;width:36px"></div>
    <div class="field" style="left:77px;top:152px;width:153px;height:24px">Your email*</div>
    <div class="btn" style="left:99px;top:190px;width:96px;height:24px">SUBSCRIBE</div>
  </div>

  <div class="contact">
    <h2 class="section-title">Contact Us</h2>
    <div class="title-rule" style="left:542px;top:46px;width:36px"></div>
    <div class="field" style="left:410px;top:72px;width:95px;height:19px;padding:6px 9px">First name *</div>
    <div class="field" style="left:514px;top:72px;width:95px;height:19px;padding:6px 9px">Last name *</div>
    <div class="field" style="left:410px;top:101px;width:95px;height:19px;padding:6px 9px">Your mail *</div>
    <div class="field" style="left:514px;top:101px;width:95px;height:19px;padding:6px 9px">Phone number *</div>
    <div class="field" style="left:410px;top:130px;width:199px;height:51px;padding:6px 9px">Message...</div>
    <div class="btn" style="left:464px;top:227px;width:96px;height:24px">SEND MESSAGE</div>
  </div>
</section>

<div class="page-foot"></div>

</body>
</html>
```